The Leadership Horizon Business Card

We need an attractive business card with the logo that we bought from ArtQuarry last year.
Our mission is to contribute to change the way today's leaders manage business companies bringing value to the workplace and helping them to build a new model of creating wealth.
Our logo is clear about our values : we seek Positive Change through People and are convinced that the pursuit of individual well-being and the chase of economic results can converge with the right management.
Industry/Entity Type
Management Consulting
Contact Information for Business Card
Corinne Valbrec
+34 612 80 27 35
corinne.valbrec@leadershiphorizonexample.com
www.leadershiphorizonexample.com
Look and feel
Each slider illustrates characteristics of the customer's brand and the style your logo design should communicate.

```html
<!DOCTYPE html>
<html lang="en">
<head>
<meta charset="utf-8">
<title>The Leadership Horizon – Business Card</title>
<link href="https://fonts.googleapis.com/css2?family=Josefin+Sans:wght@300;400;600&family=Montserrat:wght@400;500&display=swap" rel="stylesheet">
<style>
  :root {
    --page: #ffffff;
    --front-teal: #34b9a3;
    --back-mint: #d0e9e4;
    --brand-teal: #2b8a84;
    --ink: #111111;
    --white: #ffffff;
  }
  * { margin: 0; padding: 0; box-sizing: border-box; }
  html, body {
    width: 1200px;
    height: 773px;
    overflow: hidden;
    background: var(--page);
  }
  .canvas {
    position: relative;
    width: 1200px;
    height: 773px;
  }
  .card {
    position: absolute;
    left: 330px;
    width: 546px;
    height: 310px;
    border-radius: 16px;
    overflow: hidden;
    text-align: center;
  }
  .card--front {
    top: 63px;
    background: var(--front-teal);
  }
  .card--back {
    top: 409px;
    background: var(--back-mint);
  }
  .person-name {
    position: absolute;
    top: 50px;
    width: 100%;
    font-family: "Josefin Sans", sans-serif;
    font-weight: 300;
    font-size: 35px;
    letter-spacing: 1px;
    color: var(--white);
    text-transform: uppercase;
  }
  .person-role {
    position: absolute;
    top: 90px;
    width: 100%;
    font-family: "Montserrat", sans-serif;
    font-weight: 500;
    font-size: 15px;
    letter-spacing: 7.2px;
    color: var(--ink);
    text-transform: uppercase;
  }
  .contact-list {
    position: absolute;
    top: 146px;
    width: 100%;
    list-style: none;
    font-family: "Montserrat", sans-serif;
    font-size: 13.5px;
    line-height: 20.5px;
    color: var(--white);
  }
  .brand-mark {
    position: absolute;
    top: 64px;
    left: 50%;
    transform: translateX(-50%);
  }
  .brand-name {
    position: absolute;
    top: 160px;
    width: 100%;
    font-family: "Josefin Sans", sans-serif;
    font-weight: 600;
    font-size: 29px;
    letter-spacing: 1px;
    color: var(--brand-teal);
    text-transform: uppercase;
  }
  .brand-web {
    position: absolute;
    top: 220px;
    width: 100%;
    font-family: "Montserrat", sans-serif;
    font-size: 10.5px;
    letter-spacing: 3.2px;
    color: var(--brand-teal);
    text-transform: uppercase;
  }
</style>
</head>
<body>
<main class="canvas">
  <section class="card card--front" aria-label="Business card front">
    <h1 class="person-name">Corinne Valbrec</h1>
    <p class="person-role">Creative Director</p>
    <ul class="contact-list">
      <li>+34 612 80 27 35</li>
      <li>corinne.valbrec@leadershiphorizonexample.com</li>
      <li>www.leadershiphorizonexample.com</li>
    </ul>
  </section>

  <section class="card card--back" aria-label="Business card back">
    <svg class="brand-mark" width="70" height="70" viewBox="0 0 70 70" aria-hidden="true">
      <circle cx="35" cy="35" r="32" fill="var(--brand-teal)"/>
    </svg>
    <p class="brand-name">The Leadership Horizon</p>
    <p class="brand-web">www.leadershiphorizonexample.com</p>
  </section>
</main>
</body>
</html>
```